Business cards, envelopes and letterhead
Simple but professional
Business cards, envelopes and letterhead -
Creative Brief
Professional
Martin Doyle
President & CEO
4273 Beldon Street Kelsford, NB V4K 7N2 Canada
mdoyle@fernobrix.com
www.fernobrix.com
On the back, we want at least the logo (maybe the styled water drop only, we might not need the "FERNOBRIX" there but that's up to the designer), and we want to have a lot of white space so people can make notes on this when decided (though we don't need lines on the back for writing or so).

```html
<!DOCTYPE html>
<html lang="en">
<head>
<meta charset="utf-8">
<title>Fernobrix Business Card</title>
<link rel="stylesheet" href="https://fonts.googleapis.com/css2?family=Arimo:wght@400;700&display=swap">
<style>
  :root {
    --page-bg: #ffffff;
    --card-teal: #a6e3d9;
    --card-light: #e9f8f5;
    --ink-navy: #1c4f92;
    --ink-blue: #1f7fc4;
    --ink-sky: #2fa4d8;
    --rule: #5a8fc0;
  }
  * { margin: 0; padding: 0; box-sizing: border-box; }
  html, body {
    width: 1200px; height: 857px; overflow: hidden;
    background: var(--page-bg);
    font-family: "Arimo", Arial, sans-serif;
  }
  .canvas { position: relative; width: 1200px; height: 857px; }
  .card {
    position: absolute; top: 58px; width: 504px; height: 285px;
    background: linear-gradient(100deg, var(--card-teal) 0%, #b8eae1 45%, var(--card-light) 100%);
    box-shadow: 0 2px 6px rgba(0,0,0,0.12);
    overflow: hidden;
  }
  .card--front { left: 84px; }
  .card--back { left: 632px; }

  .brand { position: absolute; left: 62px; top: 88px; display: flex; align-items: center; gap: 12px; }
  .brand__mark { width: 52px; height: 52px; border-radius: 50%; background: var(--ink-blue); flex: none; }
  .brand__name { font-weight: 700; font-size: 44px; line-height: 52px; color: var(--ink-navy); letter-spacing: 2px; }

  .address { position: absolute; left: 127px; top: 146px; width: 112px; color: var(--ink-navy); font-style: normal; }
  .address__line { font-size: 10px; font-weight: 700; line-height: 12px; }
  .address__big { font-size: 21px; font-weight: 700; line-height: 23px; }

  .divider { position: absolute; left: 247px; top: 146px; width: 1px; height: 116px; background: var(--rule); }

  .contact { position: absolute; left: 258px; top: 144px; color: var(--ink-navy); }
  .contact__name { font-size: 25px; font-weight: 700; color: var(--ink-blue); line-height: 28px; }
  .contact__title { font-size: 17px; font-weight: 700; line-height: 21px; }
  .contact__phone { font-size: 14px; font-weight: 700; line-height: 18px; margin-top: 2px; }
  .contact__email { font-size: 10px; font-weight: 700; line-height: 14px; }

  .back-brand { position: absolute; left: 0; right: 0; top: 34px; display: flex; flex-direction: column; align-items: center; gap: 12px; }
  .back-brand__mark { width: 128px; height: 128px; border-radius: 50%; background: var(--ink-blue); }
  .back-brand__name { font-size: 20px; font-weight: 700; line-height: 24px; color: var(--ink-navy); letter-spacing: 1px; }
  .website { position: absolute; left: 0; right: 0; top: 222px; text-align: center; font-size: 19px; font-weight: 700; line-height: 24px; color: var(--ink-sky); }
</style>
</head>
<body>
<main class="canvas">
  <section class="card card--front" aria-label="Business card front">
    <div class="brand">
      <span class="brand__mark"></span>
      <span class="brand__name">FERNOBRIX</span>
    </div>
    <address class="address">
      <div class="address__line">4273 Beldon Street</div>
      <div class="address__line">Kelsford, NB</div>
      <div class="address__big">V4K 7N2</div>
      <div class="address__big">Canada</div>
    </address>
    <div class="divider"></div>
    <div class="contact">
      <div class="contact__name">Martin Doyle</div>
      <div class="contact__title">President &amp; CEO</div>
      <div class="contact__phone">Phone: 1-604-555-0148</div>
      <div class="contact__email">Email mdoyle@fernobrix.com</div>
    </div>
  </section>

  <section class="card card--back" aria-label="Business card back">
    <div class="back-brand">
      <span class="back-brand__mark"></span>
      <span class="back-brand__name">FERNOBRIX</span>
    </div>
    <div class="website">www.fernobrix.com</div>
  </section>
</main>
</body>
</html>
```